New Architectural Firm Business Cards

New Business card to compliment previous pixel forum logo (attached). Please design a business card that is simple, modern, creative....please do not use "symbols", simply the logo and associated graphics/text. The front should contain name/address/phone/email/web address (with graphics).....back should be 100% graphic design using the logo somehow. Hoping for a two color (black and yellow) design. full bleed design, no borders

Target Market(s)

Commercial Architecture Clients

Industry/Entity Type

Architecture

Contact Information for Business Card

Please design a business card that is simple, modern, creative....please do not use "symbols", simply the logo and associated graphics/text. The front should contain name/address/phone/email/web address (with graphics).....back should be 100% graphic design using the logo somehow

Font styles to use
Sans Serif

Colors
FFF300
FFF600
FEFA6F
FFFEC7
FFFEE8

Requirements
Must have
• Clean, Modern Design
Should not have
• Stock images or "icons"

```html
<!DOCTYPE html>
<html lang="en">
<head>
<meta charset="utf-8">
<title>Halden Architecture — Business Cards</title>
<link rel="stylesheet" href="https://fonts.googleapis.com/css2?family=Montserrat:wght@400;500;700&display=swap">
<style>
  :root {
    --stage: #e4e8ee;
    --paper: #ffffff;
    --ink: #1b1b1b;
    --ink-soft: #2a2a2a;
    --night: #161616;
    --yellow: #f2c21b;
    --white: #ffffff;
  }
  * { box-sizing: border-box; margin: 0; padding: 0; }
  html, body {
    width: 1200px; height: 675px; overflow: hidden;
    background: var(--stage);
    font-family: "Montserrat", sans-serif;
  }
  .stage {
    position: relative; width: 1200px; height: 675px;
    display: flex; align-items: center; justify-content: center; gap: 60px;
  }
  .card {
    position: relative; width: 510px; height: 292px; overflow: hidden;
    box-shadow: 0 6px 18px rgba(0,0,0,0.18);
  }

  /* Front */
  .card--front { background: var(--paper); color: var(--ink); }
  .front__identity { position: absolute; top: 42px; width: 100%; text-align: center; }
  .front__name { font-weight: 700; font-size: 26px; letter-spacing: 0.5px; }
  .front__role { font-weight: 400; font-size: 17px; letter-spacing: 1px; margin-top: 2px; }
  .front__address {
    position: absolute; top: 122px; width: 100%; text-align: center;
    font-size: 14px; line-height: 18px; font-weight: 500;
  }
  .front__icons {
    position: absolute; top: 170px; width: 100%;
    display: flex; justify-content: center; gap: 16px;
  }
  .icon { width: 26px; height: 26px; }
  .front__contacts {
    position: absolute; left: 28px; bottom: 30px;
    font-size: 15px; font-weight: 500; letter-spacing: 0.6px;
  }
  .front__band { position: absolute; left: 0; bottom: 0; width: 100%; height: 22px; }

  /* Back */
  .card--back {
    background: radial-gradient(ellipse at 30% 40%, #231c18 0%, var(--night) 60%);
    color: var(--white);
  }
  .back__brand {
    position: absolute; top: 100px; left: 0; width: 100%;
    display: flex; align-items: center; justify-content: center; gap: 12px;
  }
  .back__dot { width: 18px; height: 18px; border-radius: 50%; background: var(--yellow); }
  .back__name {
    font-weight: 700; font-size: 30px; color: var(--yellow);
    letter-spacing: 0.5px; text-transform: uppercase;
  }
  .back__web {
    position: absolute; top: 196px; width: 100%; text-align: center;
    font-size: 15px; letter-spacing: 7px; font-weight: 400;
  }
</style>
</head>
<body>
<main class="stage">
  <section class="card card--front" aria-label="Card front">
    <div class="front__identity">
      <p class="front__name">ANNA REID</p>
      <p class="front__role">FOUNDER</p>
    </div>
    <p class="front__address">PO Box 5821, Marlow Lane<br>Northgate Central 2040</p>
    <div class="front__icons">
      <svg class="icon" viewBox="0 0 26 26" aria-label="Phone">
        <circle cx="13" cy="13" r="13" fill="var(--ink)"/>
        <path d="M8 10.5c0-1.5 2.2-2.5 5-2.5s5 1 5 2.5l-1.6.6-.6-1.4c-1.8-.5-3.8-.5-5.6 0l-.6 1.4zM9.5 12h7l1 5h-9z" fill="var(--white)"/>
      </svg>
      <svg class="icon" viewBox="0 0 26 26" aria-label="Email">
        <circle cx="13" cy="13" r="13" fill="var(--ink)"/>
        <rect x="7" y="9" width="12" height="8" fill="none" stroke="var(--white)" stroke-width="1.4"/>
        <path d="M7 9l6 5 6-5" fill="none" stroke="var(--white)" stroke-width="1.4"/>
      </svg>
      <svg class="icon" viewBox="0 0 26 26" aria-label="Website">
        <circle cx="13" cy="13" r="13" fill="var(--ink)"/>
        <g fill="none" stroke="var(--white)" stroke-width="1.2">
          <circle cx="13" cy="13" r="6"/>
          <ellipse cx="13" cy="13" rx="2.6" ry="6"/>
          <path d="M7 13h12M8 10h10M8 16h10"/>
        </g>
      </svg>
    </div>
    <p class="front__contacts">0412 380 947 | hello@haldenarch.com | www.haldenarch.com</p>
    <svg class="front__band" viewBox="0 0 510 22" preserveAspectRatio="none" aria-hidden="true">
      <polygon points="0,12 232,12 228,22 0,22" fill="var(--ink-soft)"/>
      <polygon points="240,12 510,0 510,10 236,22" fill="var(--yellow)"/>
    </svg>
  </section>

  <section class="card card--back" aria-label="Card back">
    <div class="back__brand">
      <span class="back__dot"></span>
      <span class="back__name">Halden Architecture</span>
    </div>
    <p class="back__web">www.haldenarch.com</p>
  </section>
</main>
</body>
</html>
```